Business card and stationery for an eCommerce store
Vornel Home Solutions
Business card and stationery for an eCommerce store - Retailers
Creative Brief
Simple
Tarin Velo K.M
Managing Partner
Vornel Home Solutions #254 , 6th B Cross, G D Layout, Hosadiga Ext, Kelnavadi, Bangalore - 560481
pkelmandro@vomta.in
www.vomta.in
Vornel Home Solutions is the private limited firm that owns vomta.in. Vornel Home Solutions doesn't have any separate identity/ logo created. In addition to business card design, I would also like to see designs for Letterhead and Envelope.
Concepts
Business Cards/Letterhead/ Envelopes/Notepads/Tshirt/labels for copper kite crate

```html
<!DOCTYPE html>
<html lang="en">
<head>
<meta charset="utf-8">
<title>Vornel Home Solutions – Business Card</title>
<link href="https://fonts.googleapis.com/css2?family=Open+Sans:wght@400;600;700;800&display=swap" rel="stylesheet">
<style>
  :root {
    --bg: #2b2b2d;
    --card-white: #ffffff;
    --card-red: #b3122b;
    --card-red-dark: #8e0c20;
    --brand-orange: #e0721e;
    --brand-gold: #d9a23a;
    --title-red: #c4202f;
    --text-grey: #7a7a7a;
    --text-dark: #4a4a4a;
  }
  * { margin: 0; padding: 0; box-sizing: border-box; }
  html, body { width: 1200px; height: 901px; overflow: hidden; }
  body {
    background: var(--bg);
    font-family: "Open Sans", Arial, sans-serif;
    display: flex;
    flex-direction: column;
    align-items: center;
    justify-content: center;
    gap: 40px;
  }
  .card {
    position: relative;
    width: 700px;
    height: 400px;
    border-radius: 22px;
    overflow: hidden;
  }
  /* Back side */
  .card--back {
    background: linear-gradient(160deg, var(--card-red) 0%, var(--card-red-dark) 100%);
    display: flex;
    align-items: center;
    justify-content: center;
  }
  .card--back .brand-name {
    font-size: 78px;
    color: var(--brand-gold);
  }
  /* Front side */
  .card--front { background: var(--card-white); }
  .brand-name {
    font-weight: 800;
    color: var(--brand-orange);
    letter-spacing: -1px;
    line-height: 1;
  }
  .card--front .brand-name {
    position: absolute;
    left: 44px;
    top: 34px;
    font-size: 58px;
  }
  .company {
    position: absolute;
    left: 44px;
    top: 126px;
    width: 260px;
  }
  .company__name {
    font-size: 17px;
    font-weight: 700;
    color: var(--title-red);
    margin-bottom: 6px;
  }
  .company__address {
    font-size: 12px;
    color: var(--text-grey);
    line-height: 1.45;
  }
  .accent-curve {
    position: absolute;
    left: 30px;
    top: 232px;
  }
  .contact-list {
    position: absolute;
    left: 44px;
    top: 246px;
    list-style: none;
    font-size: 12.5px;
    color: var(--text-dark);
    line-height: 1.55;
  }
  .contact-list li { display: flex; align-items: center; gap: 8px; }
  .contact-list svg { flex: none; }
  .person {
    position: absolute;
    left: 390px;
    top: 200px;
  }
  .person__name {
    font-size: 21px;
    font-weight: 700;
    color: var(--title-red);
  }
  .person__role {
    font-size: 13px;
    font-weight: 600;
    color: var(--brand-orange);
  }
  .footer-rule {
    position: absolute;
    left: 44px;
    right: 160px;
    top: 338px;
    height: 2px;
    background: linear-gradient(90deg, var(--brand-gold), var(--brand-orange) 70%, rgba(224,114,30,0));
  }
  .website {
    position: absolute;
    left: 90px;
    top: 350px;
    font-size: 14px;
    font-weight: 700;
    letter-spacing: 6px;
    color: var(--title-red);
  }
</style>
</head>
<body>

  <section class="card card--back">
    <span class="brand-name">vomta.in</span>
  </section>

  <section class="card card--front">
    <span class="brand-name">vomta.in</span>

    <div class="company">
      <p class="company__name">Vornel Home Solutions</p>
      <p class="company__address">#254 , 6th B Cross,<br>G D Layout,<br>Hosadiga Ext,<br>Kelnavadi,<br>Bangalore - 560481</p>
    </div>

    <ul class="contact-list">
      <li>
        <svg width="12" height="12" viewBox="0 0 12 12"><path d="M2 1h2.5l1 2.5-1.3 1a6 6 0 0 0 3.3 3.3l1-1.3 2.5 1V11C5 11 1 7 1 2z" fill="var(--title-red)"/></svg>
        080-41926058
      </li>
      <li>
        <svg width="12" height="12" viewBox="0 0 12 12"><rect x="3" y="0.5" width="6" height="11" rx="1.2" fill="none" stroke="var(--title-red)" stroke-width="1.3"/><circle cx="6" cy="9.6" r="0.8" fill="var(--title-red)"/></svg>
        +91 9740352816
      </li>
      <li>
        <svg width="12" height="12" viewBox="0 0 12 12"><rect x="0.7" y="2.2" width="10.6" height="7.6" rx="1" fill="none" stroke="var(--title-red)" stroke-width="1.2"/><path d="M1 3l5 3.6L11 3" fill="none" stroke="var(--title-red)" stroke-width="1.2"/></svg>
        pkelmandro@vomta.in
      </li>
    </ul>

    <svg class="accent-curve" width="330" height="16" viewBox="0 0 330 16" aria-hidden="true">
      <path d="M0 12 Q120 2 330 8" fill="none" stroke="var(--brand-gold)" stroke-width="2"/>
    </svg>

    <div class="person">
      <p class="person__name">Tarin Velo K.M</p>
      <p class="person__role">Managing Partner</p>
    </div>

    <div class="footer-rule"></div>
    <p class="website">www.vomta.in</p>
  </section>

</body>
</html>
```